Flyer for Roadhaven 41Ter - Fresh Food Vending Machine in Helchteren

Project Description:
Roadhaven 41Ter has placed a new fresh food vending machine in Helchteren at KP Sodas (Lindeweg 517). We want to create an eye-catching, modern flyer to inform local residents about this vending machine and invite them to visit. The flyer will be distributed door-to-door in Helchteren.
Target Audience:
Residents of Helchteren and surrounding areas.
People looking for quick, fresh meals such as daily specials, wraps, poke bowls, soups, and pasta dishes.
Key Message:
Main title: "Helchteren, we’re here!"
Location: "Our brand-new fresh food vending machine is now at KP Sodas, Lindeweg 517!"
Available products: "Daily specials, wraps, poke bowls, soups, pasta dishes, and more."
Promotion: "For a limited time: with every product, you’ll receive a scratch card, and you always win!"
Style Guidelines:
Clean, professional, and inviting design.
Follow the new branding style of Roadhaven 41Ter (refer to the most recent posts on our Instagram and Facebook pages). Or see attachment for the layout inspiration.
Instagram: www.pictagram-example.com/roadhaven41ter
Facebook: www.friendbook-example.com/Roadhaven41
Do not use the older branding visible in earlier posts.
Format:
Flyer size: A5 (148 x 210 mm).
Additional Information:
Include our logos and social media accounts on the flyer.
Add a clear call-to-action, such as: "Visit us today!"
Ensure the flyer is easy to read and that all information is clear at a glance.
We look forward to seeing your creative and inspiring designs!

```html
<!DOCTYPE html>
<html lang="en">
<head>
<meta charset="utf-8">
<title>Roadhaven 41Ter – Helchteren Flyer</title>
<link rel="stylesheet" href="https://fonts.googleapis.com/css2?family=Roboto:wght@400;500;700;900&display=swap">
<style>
  :root {
    --page: #eef0f3;
    --blue: #1c4fa5;
    --blue-deep: #173f8c;
    --red: #e8432a;
    --red-dark: #d5361f;
    --white: #ffffff;
    --machine-dark: #3a3f47;
    --machine-light: #8a9099;
  }
  * { box-sizing: border-box; margin: 0; padding: 0; }
  html, body { width: 1200px; height: 1200px; overflow: hidden; background: var(--page); }
  body { position: relative; font-family: "Roboto", Arial, sans-serif; color: var(--white); }

  .flyer {
    position: absolute; left: 235px; top: 82px; width: 730px; height: 1036px;
    background: var(--red); overflow: hidden;
  }
  .flyer__top {
    position: absolute; left: 0; top: 0; width: 730px; height: 602px;
    background: linear-gradient(180deg, var(--blue-deep) 0%, var(--blue) 100%);
  }
  .machine-photo {
    position: absolute; left: 300px; top: 20px; width: 430px; height: 582px;
    background: linear-gradient(90deg, rgba(58,63,71,0) 0%, rgba(58,63,71,0.75) 35%, var(--machine-dark) 70%, var(--machine-light) 100%);
  }
  .frame { position: absolute; }
  .frame--red-top { left: 47px; top: 77px; width: 377px; height: 4px; background: var(--red); }
  .frame--red-side { left: 47px; top: 77px; width: 4px; height: 126px; background: var(--red); }
  .frame--white { left: 458px; top: 77px; width: 228px; height: 316px; border-right: 4px solid var(--white); border-bottom: 4px solid var(--white); }
  .frame--white-top { left: 650px; top: 77px; width: 36px; height: 4px; background: var(--white); }

  .brand {
    position: absolute; left: 432px; top: 44px; width: 226px; height: 56px;
    display: flex; align-items: center; justify-content: center;
    background: var(--blue-deep);
    font-weight: 900; font-size: 21px; letter-spacing: 0.3px; color: var(--white);
    text-transform: uppercase; white-space: nowrap;
  }

  .headline__place { position: absolute; left: 47px; top: 216px; font-size: 42px; font-weight: 500; letter-spacing: 0.5px; line-height: 1; }
  .headline__main { position: absolute; left: 45px; top: 258px; font-size: 76px; font-weight: 900; color: var(--red); line-height: 1; letter-spacing: -0.5px; white-space: nowrap; }
  .headline__intro { position: absolute; left: 47px; top: 344px; font-size: 21px; line-height: 1.28; white-space: nowrap; }

  .products__title {
    position: absolute; left: 169px; top: 433px; width: 391px; height: 58px;
    background: var(--red); display: flex; align-items: center; justify-content: center;
    font-size: 30px; font-weight: 700; letter-spacing: 0.3px;
  }
  .product { position: absolute; top: 522px; width: 128px; }
  .product__photo { width: 128px; height: 161px; border: 3px solid var(--white); border-radius: 16px; }
  .product__name { margin-top: 18px; text-align: center; font-size: 17px; font-weight: 700; white-space: nowrap; }
  .product--wraps { left: 47px; }
  .product--poke { left: 217px; }
  .product--soups { left: 387px; }
  .product--pasta { left: 557px; }
  .product--wraps .product__photo { background: linear-gradient(135deg, #e9d9b8, #d8a24a 60%, #8a5a3a); }
  .product--poke .product__photo { background: linear-gradient(135deg, #e6e2da, #c9b79a 50%, #7f9a55); }
  .product--soups .product__photo { background: linear-gradient(135deg, #3b3430, #c8742c 55%, #2e2a27); }
  .product--pasta .product__photo { background: linear-gradient(135deg, #1f1f22, #a8643a 55%, #1a1a1c); }

  .promo { position: absolute; left: 109px; top: 772px; width: 512px; height: 94px; background: var(--blue); }
  .promo__label {
    position: absolute; left: 259px; top: 749px; width: 212px; height: 45px; background: var(--white);
    display: flex; align-items: center; justify-content: center;
    font-size: 27px; font-weight: 700; color: var(--red);
  }
  .promo__text { position: absolute; left: 109px; top: 806px; width: 512px; text-align: center; font-size: 15.5px; line-height: 1.4; letter-spacing: 0.2px; }
  .promo__text strong { font-weight: 700; }

  .cta { position: absolute; left: 47px; top: 892px; width: 639px; display: flex; align-items: center; gap: 8px; }
  .cta__rule { flex: 1; height: 2px; background: var(--white); margin-top: 12px; }
  .cta__text { font-size: 31px; font-weight: 700; white-space: nowrap; }

  .contact { position: absolute; left: 47px; top: 930px; width: 639px; height: 62px; background: var(--red-dark); }
  .contact__call { position: absolute; left: 0; top: 0; width: 269px; height: 62px; background: var(--blue); }
  .contact__call svg { position: absolute; left: 28px; top: 14px; }
  .contact__label { position: absolute; left: 75px; top: 11px; font-size: 11px; }
  .contact__phone { position: absolute; left: 75px; top: 25px; font-size: 24px; font-weight: 700; white-space: nowrap; }
  .contact__item { position: absolute; display: flex; align-items: center; gap: 6px; font-size: 10px; line-height: 1; white-space: nowrap; }
  .contact__item svg { flex: none; }
  .contact__item--social { left: 290px; top: 13px; }
  .contact__item--mail { left: 290px; top: 38px; }
  .contact__item--web { left: 462px; top: 13px; }
  .contact__item--address { left: 462px; top: 38px; }
  .flyer__rule { position: absolute; left: 47px; top: 1004px; width: 639px; height: 1px; background: var(--white); }
</style>
</head>
<body>
  <main class="flyer">
    <div class="flyer__top"></div>
    <div class="machine-photo" role="img" aria-label="Fresh food vending machine installed at KP Sodas"></div>

    <span class="frame frame--red-top"></span>
    <span class="frame frame--red-side"></span>
    <span class="frame frame--white"></span>
    <span class="frame frame--white-top"></span>

    <div class="brand">Roadhaven 41Ter</div>

    <h1 class="headline__place">HELCHTEREN</h1>
    <p class="headline__main">WE'RE HERE!</p>
    <p class="headline__intro">Our brand New fresh Food Vending Machine<br>is now at KP Sodas, Lindeweg 517!</p>

    <h2 class="products__title">AVAILABLE PRODUCTS</h2>
    <div class="product product--wraps">
      <div class="product__photo" role="img" aria-label="Wraps with fresh filling"></div>
      <p class="product__name">WRAPS</p>
    </div>
    <div class="product product--poke">
      <div class="product__photo" role="img" aria-label="Poke bowl with rice, salmon and vegetables"></div>
      <p class="product__name">POKE BOWLS</p>
    </div>
    <div class="product product--soups">
      <div class="product__photo" role="img" aria-label="Bowl of pumpkin soup"></div>
      <p class="product__name">SOUPS</p>
    </div>
    <div class="product product--pasta">
      <div class="product__photo" role="img" aria-label="Plate of noodle pasta dish"></div>
      <p class="product__name">PASTA DISHES</p>
    </div>

    <div class="promo"></div>
    <div class="promo__label">PROMOTION!</div>
    <p class="promo__text">FOR A LIMITED TIME: WITH EVERY PRODUCT, YOU’LL RECEIVE A<br>SCRATCH CARD, AND <strong>YOU ALWAYS WIN!</strong></p>

    <div class="cta"><span class="cta__rule"></span><span class="cta__text">VISIT US TODAY!</span><span class="cta__rule"></span></div>

    <div class="contact">
      <div class="contact__call">
        <svg width="34" height="34" viewBox="0 0 24 24" fill="none" stroke="#fff" stroke-width="1.6" stroke-linejoin="round">
          <path d="M5 3h4l2 5-2.5 1.5a11 11 0 0 0 6 6L16 13l5 2v4a2 2 0 0 1-2 2A16 16 0 0 1 3 5a2 2 0 0 1 2-2z"/>
          <path d="M15 3a6 6 0 0 1 6 6M15 6.5A2.5 2.5 0 0 1 17.5 9"/>
        </svg>
        <span class="contact__label">Call Us:</span>
        <span class="contact__phone">+32 011 555 019</span>
      </div>
      <div class="contact__item contact__item--social">
        <svg width="11" height="11" viewBox="0 0 12 12"><rect x="1" y="1" width="10" height="10" rx="2" fill="none" stroke="#fff" stroke-width="1.4"/></svg>
        roadhaven41ter
      </div>
      <div class="contact__item contact__item--mail">
        <svg width="12" height="9" viewBox="0 0 13 10" fill="none" stroke="#fff" stroke-width="1.3"><rect x="0.7" y="0.7" width="11.6" height="8.6"/><path d="M0.7 0.7 6.5 5.5 12.3 0.7"/></svg>
        hello@roadhaven-example.eu
      </div>
      <div class="contact__item contact__item--web">
        <svg width="11" height="11" viewBox="0 0 12 12" fill="none" stroke="#fff" stroke-width="1.2"><circle cx="6" cy="6" r="5"/><ellipse cx="6" cy="6" rx="2.2" ry="5"/><path d="M1 6h10"/></svg>
        roadhaven-example.eu
      </div>
      <div class="contact__item contact__item--address">
        <svg width="9" height="12" viewBox="0 0 10 13"><path d="M5 0.5A4.3 4.3 0 0 0 0.7 4.8C0.7 8 5 12.5 5 12.5S9.3 8 9.3 4.8A4.3 4.3 0 0 0 5 0.5z" fill="#fff"/><circle cx="5" cy="4.8" r="1.6" fill="#d5361f"/></svg>
        Havenweg 8, Sampleton, Belgium
      </div>
    </div>
    <div class="flyer__rule"></div>
  </main>
</body>
</html>
```